Zielgruppe
Wir sind KQ Rapid Voltwerk GmbH mit Sitz in Basel Schweiz. Wir bieten die volle Palette von Elektronikdienstleistungen. Besonders aber Photovoltaik (Solar) auf Einfamilienhäusern und Gewerbeeinheiten, Smart Home Automation mit Dravix (Partner) und allgemeine Elektrikerdienstleistungen in Häusern und Wohnung.
USP
• Regionale Firma, BS, BL,AG
○ Daher schnelle Reaktion im Störungsfall. Garantierte Entstörung
• Umsetzung innert 2-3 Monate
• Planung und Durchführung aus einer Hand.
• Umsetzung auch in der PV Installation nur durch eigene Mitarbeiter
• Kelmora Förderung, bis zu 6TCHF
• Kompetent, freundlich
• Eidgenössich diplomierter Elektroinstallateur (Meister)
• EFZ (Eidgenösisch Fährigkeitszeugnis)
• 1 Jahr Existenz
• Dravix goldpartner
• Nur Doppelglasmodule mit 25 Jahre Garantie, 10 Jahre auf Wechselrichter und Batterie
• Planung mittels CAD/*D Planung, technische Tool
• Genaues und schnelles Angebot innert 5 Werktagen
USP:
• Stromkosten sparen
• Autark werden, unabhängig von Strompreisentwicklung
• Umwelt schützen
WUNSCHKUNDE
• Soziodemografisch
○ Eigentümer
○ Gehobene Mittelklasse
• Lokalität in Basel und Umgebung
Aufgabenstellung
Medien unter: https://files.trobelix.ch/index.php/s/mQzWnLpRtYvA7KD
Logo ist dort vorhanden.
Hintergrund hell (weiss, hellgrau bspw.)
Schriftart
Verlinkungen zu Social Media:
• Facebook
• Linkedin
• Instagram
Beispielseiten, die gefallen:
Alpin Lichtfeld Werk (alpin-lichtfeld-werk.ch) Prio
Counter mit

```html
<!DOCTYPE html>
<html lang="de">
<head>
<meta charset="utf-8">
<title>KQ Rapid Voltwerk GmbH – Photovoltaik</title>
<link rel="stylesheet" href="https://fonts.googleapis.com/css2?family=Poppins:ital,wght@0,400;0,500;0,600;0,700;0,800;1,300;1,400;1,500&display=swap">
<style>
:root{
  --green:#0b8a41;
  --green-dark:#0d5f30;
  --green-light:#a6e3bd;
  --navy:#30334a;
  --ink:#111;
  --grey:#666;
  --line:#e4e4e4;
  --white:#fff;
}
*{box-sizing:border-box;margin:0;padding:0}
html,body{width:1200px;height:3228px;overflow:hidden;background:var(--white)}
body{font-family:'Poppins',sans-serif;color:var(--ink)}
.canvas{position:relative;width:1200px;height:3228px;overflow:hidden}
.abs{position:absolute}
.btn{position:absolute;display:flex;align-items:center;justify-content:center;background:var(--green-dark);color:var(--white);font-weight:700;border-radius:5px;font-size:17px;text-decoration:none}

/* top bar */
.topbar{top:18px;left:86px;right:84px;height:22px;display:flex;align-items:center;font-size:13px;color:#444}
.topbar .item{display:flex;align-items:center;gap:10px;margin-right:26px}
.topbar .mail{font-size:11px;text-decoration:underline}
.topbar .social{margin-left:auto;display:flex;align-items:center;gap:10px;font-size:10px;color:#333}
.sq{width:15px;height:15px;border-radius:3px;display:inline-block}

/* header */
.brand{position:absolute;display:flex;align-items:center;gap:10px;font-weight:500;color:var(--ink)}
.brand .dot{width:46px;height:46px;border-radius:50%;background:var(--green);flex:none}
.brand .name{font-size:16px;line-height:1.15}
.nav{top:84px;left:383px;display:flex;gap:34px;font-size:18px;font-weight:500;letter-spacing:1.6px;color:var(--navy)}
.nav .active{color:var(--green);font-weight:700}
.nav .refs{color:#4a5a3a}

/* hero */
.hero-title{top:190px;left:96px;width:620px;font-size:35px;font-weight:800;line-height:53px;color:var(--green)}
.hero-title .dark{color:var(--ink)}
.hero-sub{top:366px;left:90px;width:520px;font-size:22px;line-height:32px;color:#555}
.hero-band{top:650px;left:0;width:1200px;height:74px;background:linear-gradient(90deg,rgba(166,227,189,0) 5%,#bfeacf 50%,#98dcb2 100%)}
.dots{position:absolute;display:flex;gap:8px}
.dots span{height:9px;border-radius:5px;background:#fff}

/* stats */
.stat{position:absolute;top:759px;width:232px;height:224px}
.stat .shape{position:absolute;inset:0;background:var(--green);border-radius:26px;transform:skewX(-9deg);box-shadow:3px 6px 8px rgba(0,0,0,.3)}
.stat .body{position:relative;height:100%;display:flex;flex-direction:column;align-items:center;color:var(--white);text-align:center;padding-top:16px}
.stat .num{font-size:31px;font-weight:800;line-height:36px;margin-top:8px}
.stat .unit{font-size:16px;font-weight:700;align-self:flex-end;margin-right:34px;line-height:18px}
.stat .label{font-size:17px;line-height:24px;margin-top:10px;font-weight:500}

/* quotes */
.section-title{font-size:32px;font-weight:800;color:var(--green);letter-spacing:.5px}
.qcard{position:absolute;background:var(--white);border-radius:16px;box-shadow:0 3px 7px rgba(0,0,0,.18);text-align:center}
.qcard .text{font-size:14px;line-height:21px;color:#222}
.qcard.side .text{color:#777;font-size:13.5px}
.qmark{position:absolute;font-size:110px;font-weight:800;color:var(--green);line-height:1;height:60px;overflow:hidden}
.person{display:flex;align-items:center;gap:16px;text-align:left}
.avatar{width:93px;height:93px;border-radius:50%;flex:none}
.person .pname{font-weight:700;font-size:17px}
.person .pco{font-size:17px}
.arrow{position:absolute;width:46px;height:46px;border-radius:50%;background:var(--white);box-shadow:0 2px 5px rgba(0,0,0,.3);display:flex;align-items:center;justify-content:center}

/* referenzen intro */
.kicker{top:1482px;left:104px;font-size:16px;font-weight:700;letter-spacing:1px}
.ref-title{top:1516px;left:102px;font-size:44px;font-weight:800;color:var(--green)}
.ref-text{top:1584px;left:104px;width:1020px;font-size:18px;line-height:27px}

/* gallery sections */
.gal-green{background:var(--green)}
.gal-navy{background:var(--navy)}
.gal-title{font-size:30px;font-weight:700;color:var(--white);letter-spacing:.5px}
.gal-tag{font-size:29px;font-style:italic;font-weight:500;color:var(--white);letter-spacing:3px;line-height:42px}
.photo{position:absolute;border-radius:22px;border:3px solid #f3f3f3;overflow:hidden}
.photo .overlay{position:absolute;inset:0;background:rgba(11,138,65,.72);color:var(--white);padding:0 20px;display:flex;flex-direction:column;justify-content:center}
.photo .overlay h3{font-size:21px;font-weight:800;letter-spacing:1px;margin-bottom:10px}
.photo .overlay p{font-size:18px;line-height:27px}

/* footer */
.footer{top:2897px;left:0;width:1200px;height:285px;background:var(--green);color:var(--white)}
.f-head{top:49px;left:273px;font-size:15px;font-weight:700;line-height:23px}
.f-body{top:108px;left:273px;width:270px;font-size:13.5px;line-height:21px}
.f-social{top:236px;left:273px;display:flex;gap:10px}
.f-social span{width:25px;height:25px;background:#111;border-radius:2px}
.f-social span.alt{background:#e7c24a}
.partner{top:110px;left:580px;font-size:46px;font-weight:400;color:#9fe0a9;letter-spacing:1px}
.subscribe{top:30px;left:784px;font-size:21px;font-style:italic;font-weight:300}
.sub-line{top:72px;left:784px;width:70px;height:2px;background:#bfe8cd}
.input{top:105px;left:784px;width:328px;height:50px;background:var(--white);border-radius:3px;display:flex;align-items:center;gap:12px;padding-left:14px;font-size:13.5px;color:#888}
.input .sep{width:1px;height:22px;background:#ccc}
.f-note{top:188px;left:784px;width:330px;font-size:13px;font-style:italic;font-weight:300;line-height:19px;color:#e6f6ec}
.copyright{top:3190px;left:0;width:1200px;text-align:center;font-size:14px;color:var(--green)}
</style>
</head>
<body>
<div class="canvas">

  <!-- top bar -->
  <div class="abs topbar">
    <div class="item">
      <svg width="16" height="16" viewBox="0 0 24 24"><path fill="#0b8a41" d="M6.6 10.8a15 15 0 006.6 6.6l2.2-2.2c.3-.3.7-.4 1-.2 1.1.4 2.3.6 3.6.6.6 0 1 .4 1 1V20c0 .6-.4 1-1 1A17 17 0 013 4c0-.6.4-1 1-1h3.5c.6 0 1 .4 1 1 0 1.3.2 2.5.6 3.6.1.3 0 .7-.2 1z"/></svg>
      <span>+41 61 555 0192</span>
    </div>
    <div class="item">
      <svg width="18" height="14" viewBox="0 0 24 18"><rect width="24" height="18" rx="2" fill="#0b8a41"/><path d="M2 2l10 8 10-8" stroke="#fff" stroke-width="2" fill="none"/></svg>
      <span class="mail">info@kqvoltwerk.ch</span>
    </div>
    <div class="social">
      <span>Social Media:</span>
      <span class="sq" style="background:#3b5a9a"></span>
      <span class="sq" style="background:#d6408a"></span>
      <span class="sq" style="background:#1a66b5"></span>
      <span class="sq" style="background:#111"></span>
    </div>
  </div>

  <!-- header -->
  <div class="brand" style="top:72px;left:82px">
    <span class="dot"></span>
    <span class="name">KQ Rapid<br>Voltwerk GmbH</span>
  </div>
  <nav class="abs nav">
    <span class="active">Homepage</span>
    <span class="refs">Referenzen</span>
    <span>Dienstleistungen &nbsp;<b style="font-size:24px;line-height:18px">+</b></span>
  </nav>
  <a class="btn" style="top:78px;left:1011px;width:103px;height:44px;font-size:17px;letter-spacing:.5px">KONTAKT</a>

  <!-- hero -->
  <div class="abs hero-band"></div>
  <svg class="abs" style="top:160px;left:507px" width="693" height="531" viewBox="0 0 693 531" role="img" aria-label="Photovoltaik-Module auf einem Dach unter hellem Himmel">
    <defs>
      <linearGradient id="panel" x1="0" y1="1" x2="1" y2="0">
        <stop offset="0" stop-color="#1d2f7a"/>
        <stop offset=".5" stop-color="#3a5bb0"/>
        <stop offset=".8" stop-color="#c9d6ea"/>
        <stop offset="1" stop-color="#eef2f8"/>
      </linearGradient>
    </defs>
    <path d="M270 0H693V531H30C8 531 -6 510 4 488L240 20C248 6 258 0 270 0Z" fill="url(#panel)"/>
  </svg>
  <div class="dots" style="top:664px;left:842px">
    <span style="width:86px"></span><span style="width:88px;background:#a6e3bd"></span><span style="width:86px"></span>
  </div>
  <h1 class="abs hero-title">PHOTOVOLTAIK – IHRE SCHLÜSSEL ZUM <span class="dark">ENERGIEEINSPARUNG</span> UND <span class="dark">UMWELTSCHUTZ</span>!</h1>
  <p class="abs hero-sub">Tauchen Sie Ein In Die Welt Der Nachhaltigen Energie Mit Unserer Photovoltaik-Lösung</p>
  <a class="btn" style="top:473px;left:101px;width:143px;height:44px">Jetzt Handeln</a>

  <!-- stats -->
  <div class="stat" style="left:91px">
    <div class="shape"></div>
    <div class="body">
      <svg width="76" height="64" viewBox="0 0 76 64" fill="none" stroke="#fff" stroke-width="3"><circle cx="58" cy="12" r="5"/><path d="M58 2v3M58 19v3M48 12h3M65 12h3"/><path d="M6 34L34 14l28 20"/><path d="M12 32v24h44V32"/><rect x="22" y="42" width="10" height="14"/><circle cx="46" cy="44" r="7"/></svg>
      <div class="num">›&nbsp;100</div>
      <div class="label" style="margin-top:30px">Erzeugte Leistung<br>Für Haushal</div>
    </div>
  </div>
  <div class="stat" style="left:356px">
    <div class="shape"></div>
    <div class="body">
      <svg width="60" height="56" viewBox="0 0 60 56" fill="none" stroke="#fff" stroke-width="3"><path d="M4 10h52M8 4v10M52 4v10M18 6v8M42 6v8"/><rect x="12" y="18" width="36" height="34"/><path d="M12 30h36M24 18v34M36 18v34"/></svg>
      <div class="num">1.000.000</div>
      <div class="unit">Kwh</div>
      <div class="label">Stromproduktion Pro<br>Jahr</div>
    </div>
  </div>
  <div class="stat" style="left:619px">
    <div class="shape"></div>
    <div class="body">
      <svg width="74" height="56" viewBox="0 0 74 56" fill="none" stroke="#fff" stroke-width="3"><path d="M18 38a12 12 0 01-2-24 16 16 0 0130-4 12 12 0 0112 28z"/><text x="22" y="31" fill="#fff" stroke="none" font-size="14" font-weight="700" font-family="Poppins,sans-serif">CO₂</text><path d="M24 42v10M37 42v10M50 42v10M20 48l4 4 4-4M33 48l4 4 4-4M46 48l4 4 4-4"/></svg>
      <div class="num">&gt;&nbsp;&nbsp;1000</div>
      <div class="unit" style="margin-right:58px">t</div>
      <div class="label">Gesparte CO2<br>Emmission</div>
    </div>
  </div>
  <div class="stat" style="left:883px">
    <div class="shape"></div>
    <div class="body">
      <svg width="60" height="62" viewBox="0 0 60 62" fill="none" stroke="#fff" stroke-width="3"><path d="M14 14l16-10 16 10"/><circle cx="30" cy="36" r="11"/><path d="M30 29v14M26 33h7M26 40h7"/><path d="M6 52c8-6 16 4 24 0s16-8 24-2"/><path d="M46 4v14M42 14l4 4 4-4"/></svg>
      <div class="num">12.3</div>
      <div class="unit" style="margin-right:22px;font-size:17px">kw/h</div>
      <div class="label" style="font-size:16px;line-height:24px">Durchschnittliche<br>Kostenersparniss In<br>Rappen Pro</div>
    </div>
  </div>

  <!-- testimonials -->
  <h2 class="abs section-title" style="top:1036px;left:0;width:1240px;text-align:center">KUNDENZITAT</h2>

  <div class="qmark" style="top:1068px;left:40px">”</div>
  <div class="qcard side" style="top:1102px;left:-60px;width:402px;height:261px;text-align:left;padding:24px 20px 0 60px">
    <p class="text">Und Insbesondere Jonas Waren Ein Wichtiger Baustein Realisierungunseres Projektoffices NORVATMEET. Nach Einem Gespräch War Marco Und Jonassofort Die Problemstellung Und Bei Auftretenden Problemen, Brachten Siedirekt Mögliche Lösungsalternativen.</p>
    <div style="margin-top:46px;font-size:17px;color:#555"><b>Lukas Brenner</b><br>Norvat.Com</div>
  </div>

  <div class="qmark" style="top:1068px;left:1168px">”</div>
  <div class="qcard side" style="top:1102px;left:980px;width:300px;height:268px;text-align:left;padding:30px 0 0 24px">
    <p class="text">KQ Rapid Und Insbesondere Jonas Bei Der Realisierungunseres Proj Initialgespräch War Marco Und Klar Und Bei Auftretenden Mögliche Lösungen</p>
    <div class="person" style="margin-top:28px">
      <div class="avatar" style="background:linear-gradient(135deg,#dcd6d0,#c45a4a);width:92px;height:92px" role="img" aria-label="Porträtfoto einer Kundin am Schreibtisch"></div>
      <div style="color:#666"><div class="pname">Lukas</div><div class="pco">Norvat.C</div></div>
    </div>
  </div>

  <div class="qcard" style="top:1134px;left:403px;width:485px;height:275px;padding:36px 20px 0">
    <div class="qmark" style="top:-22px;left:210px">”</div>
    <p class="text">KQ Rapid Und Insbesondere Jonas Waren Ein Wichtiger Baustein Bei Der Realisierungunseres Projektoffices NORVATMEET. Nach Einem Initialgespräch War Marco Und Jonassofort Die Problemstellung Klar Und Bei Auftretenden Problemen, Brachten Siedirekt Mögliche Lösungsalternativen.</p>
    <div class="person" style="margin:16px 0 0 12px">
      <div class="avatar" style="background:linear-gradient(160deg,#6f7f94,#2d3a52)" role="img" aria-label="Porträtfoto des zitierten Kunden"></div>
      <div><div class="pname">Lukas Brenner</div><div class="pco">Norvat.Com</div></div>
    </div>
  </div>
  <div class="arrow" style="top:1249px;left:380px"><svg width="14" height="18" viewBox="0 0 14 18"><path d="M10 2L3 9l7 7" stroke="#0b8a41" stroke-width="2.5" fill="none"/></svg></div>
  <div class="arrow" style="top:1249px;left:864px"><svg width="14" height="18" viewBox="0 0 14 18"><path d="M4 2l7 7-7 7" stroke="#0b8a41" stroke-width="2.5" fill="none"/></svg></div>

  <!-- referenzen intro -->
  <div class="abs" style="top:1457px;left:106px;width:63px;height:4px;background:var(--ink)"></div>
  <div class="abs kicker">UNSERE ANGEBOTE FÜR EINE NACHHALTIGE ZUKUNFT</div>
  <h2 class="abs ref-title">REFERENZEN</h2>
  <p class="abs ref-text">Sparen Sie Nicht Nur Kosten, Sondern Gestalten Sie Aktiv Eine Grünere Zukunft. Erfahren Sie, Wie Sie Unabhängig Von Steigenden Strompreisen Werden Und Dabei Die Umwelt Schützen Können</p>
  <a class="btn" style="top:1667px;left:91px;width:202px;height:44px">Kontakt Aufnehmen</a>

  <!-- gallery: Mehrfamilienhaus -->
  <div class="abs gal-green" style="top:1782px;left:0;width:512px;height:276px"></div>
  <div class="abs gal-navy" style="top:1782px;left:512px;width:673px;height:160px"></div>
  <div class="abs gal-title" style="top:1818px;left:137px">MEHRFAMILIENHAUS</div>
  <div class="abs" style="top:1809px;left:589px;width:50px;height:4px;background:var(--green)"></div>
  <div class="abs gal-tag" style="top:1816px;left:585px">UNSERE ANGEBOTE FÜR EINE<br>NACHHALTIGE ZUKUNFT</div>

  <div class="photo" style="top:1939px;left:145px;width:311px;height:289px;background:linear-gradient(180deg,#e3e8ee 0%,#cfd6de 45%,#2b3240 70%,#4b4240 100%)" role="img" aria-label="Dunkle Solarmodule auf einem Ziegelhaus"></div>
  <div class="photo" style="top:1939px;left:476px;width:309px;height:289px;background:linear-gradient(180deg,#9fc7c0,#6f8f7e)" role="img" aria-label="Mehrfamilienhaus mit Solaranlage">
    <div class="overlay"><h3>MEHRFAMILIENHAUS</h3><p>15.84 kWp<br>Aesch Auftraggeber:<br>Brändli Aesch</p></div>
  </div>
  <div class="photo" style="top:1939px;left:804px;width:312px;height:289px;background:linear-gradient(180deg,#dfe6ef 0%,#cdd6e2 50%,#384050 72%,#a69c88 100%)" role="img" aria-label="Einfamilienhaus mit Solarmodulen auf dem Dach"></div>
  <div class="photo" style="top:1939px;left:1140px;width:100px;height:289px;background:linear-gradient(180deg,#6a7284,#d8dccb 55%,#8aa268)" role="img" aria-label="Haus mit Garten"></div>
  <div class="dots" style="top:2277px;left:155px;gap:3px">
    <span style="width:30px;background:#aaa"></span><span style="width:30px;background:var(--green-light)"></span><span style="width:30px;background:#aaa"></span>
  </div>
  <a class="btn" style="top:2261px;left:995px;width:122px;height:44px">Mehr Sehen</a>

  <!-- gallery: öffentliches Gebäude -->
  <div class="abs gal-green" style="top:2351px;left:0;width:515px;height:276px"></div>
  <div class="abs gal-navy" style="top:2351px;left:515px;width:673px;height:160px"></div>
  <div class="abs gal-title" style="top:2387px;left:80px">ÖFFENTLICHES GEBÄUDE</div>
  <div class="abs" style="top:2378px;left:592px;width:50px;height:4px;background:var(--green)"></div>
  <div class="abs gal-tag" style="top:2385px;left:588px">UNSERE ANGEBOTE FÜR EINE<br>NACHHALTIGE ZUKUNFT</div>

  <div class="photo" style="top:2483px;left:147px;width:311px;height:289px;background:linear-gradient(180deg,#c7d9ee 0%,#9fb3c8 40%,#8a95a0 70%,#3c4a66 100%)" role="img" aria-label="Hochhaus mit Solarfeld im Vordergrund"></div>
  <div class="photo" style="top:2483px;left:478px;width:311px;height:289px;background:linear-gradient(180deg,#2f6cc3 0%,#5d8fd6 45%,#3a4257 62%,#8a4a3a 85%,#6d6a60 100%)" role="img" aria-label="Öffentliches Gebäude mit Solaranlage"></div>
  <div class="photo" style="top:2483px;left:807px;width:312px;height:289px;background:linear-gradient(180deg,#7aa88c,#4d7a60)" role="img" aria-label="Luftbild eines öffentlichen Gebäudes">
    <div class="overlay" style="padding-top:40px"><h3>ÖFFENTLICHES GEBÄUDE</h3><p>15.84 kWp<br>Aesch Auftraggeber:<br>Brändli Aesch</p></div>
  </div>
  <div class="photo" style="top:2483px;left:1143px;width:100px;height:289px;background:linear-gradient(180deg,#aac4de,#2e3d60)" role="img" aria-label="Solarfeld"></div>
  <div class="dots" style="top:2822px;left:158px;gap:3px">
    <span style="width:30px;background:#aaa"></span><span style="width:30px;background:var(--green-light)"></span><span style="width:30px;background:#aaa"></span>
  </div>
  <a class="btn" style="top:2805px;left:997px;width:122px;height:44px">Mehr Sehen</a>

  <!-- footer -->
  <footer class="abs footer">
    <div class="brand" style="top:56px;left:85px;color:#fff">
      <span class="dot" style="background:#fff;width:40px;height:40px"></span>
      <span class="name" style="font-size:15px">KQ Rapid<br>Voltwerk GmbH</span>
    </div>
    <div class="abs f-head">ELEKTRONIK FÜR EINE<br>STRAHLENDE ZUKUNFT</div>
    <p class="abs f-body">Innovative Technologie, Umweltfreundliche Elektronik: Ihr Zuhause Wird Lebendig Mit Unseren Lösungen Für Eine Grüne, Nachhaltige Zukunft.</p>
    <div class="abs f-social"><span></span><span class="alt"></span><span></span><span></span></div>
    <div class="abs partner">Dravix</div>
    <div class="abs subscribe">Abonnieren</div>
    <div class="abs sub-line"></div>
    <div class="abs input">
      <svg width="18" height="14" viewBox="0 0 24 18"><rect x="1" y="1" width="22" height="16" rx="3" stroke="#e7b84a" stroke-width="2" fill="none"/><path d="M3 4l9 7 9-7" stroke="#e7b84a" stroke-width="2" fill="none"/></svg>
      <span class="sep"></span>
      <span>Geben sie ihre E-Mail Adresse ein</span>
    </div>
    <p class="abs f-note">Senden Sie eine E-Mail und Sie erhalten regelmäßig unsere Newsletter, Service-Blogs und Pressemitteilungen</p>
  </footer>
  <div class="abs copyright">Copyright 2024 KQ Rapid Voltwerk GmbH, All Right Reserved</div>

</div>
</body>
</html>
```